Logo Tweak & Full Set of Stationery

We need a redesign / tweaking of Logo for rebranding of our company. We are Australia's largest installer of commercial fencing and high security infrastructure. We also have divisions in security and civil works (infrastrucuture).

We would like to see designs that incorporate black, white & blue. Revamp of current Diamond Logo (including HC) would be ideal but open to all ideas.

Design needs to portray a highly professional & corporate image.

Required:
- Tweak / Redesign of Logo
- Letterhead
- email Signature
- Business Cards
- Presentation Folder

Address fields should be interchangeable to accomodate multiple locations.

Website: www.harvillecorp.com.au
Updates

Due to short turn around time for project - Fee increased to $500 AUD Guaranteed

Thanks

Designs are looking good
I have emailed those submitted thus far to the board to start short listing.

Please do not take offence if your design is eliminated as part of this process  - there are so many great concepts and if is difficult to pick between them.

Thanks
Dustin

Target Market(s)

Tier 1 / 2 Builders (ie.. Brick Arch Peter Farley) and Government related bodies

Industry/Entity Type

Security

Requirements
Must have
• Company Name: Harville Corp

Tag Line: Fencing * Security * Civil

Logo

```html
<!DOCTYPE html>
<html lang="en">
<head>
<meta charset="utf-8">
<title>Harville Corp Stationery</title>
<link href="https://fonts.googleapis.com/css2?family=Exo+2:wght@400;500&display=swap" rel="stylesheet">
<style>
  :root {
    --backdrop: #5f5d5e;
    --sheet: #f1f5f8;
    --card: #e8eaed;
    --ink: #3b3b3d;
    --muted: #6a6b6e;
    --blue: #1eaee8;
    --dark: #444446;
    --flap: #dcdde0;
    --white: #ffffff;
  }
  * { box-sizing: border-box; margin: 0; padding: 0; }
  html, body { width: 1200px; height: 686px; overflow: hidden; }
  body {
    background: var(--backdrop);
    font-family: "Exo 2", sans-serif;
    color: var(--ink);
    position: relative;
  }
  .stripe {
    position: absolute; left: 0; right: 0; bottom: 0; height: 6px;
    background: linear-gradient(to right, var(--blue) 0 58%, var(--dark) 58% 100%);
  }
  .brand { display: flex; align-items: center; gap: 7px; }
  .brand-square { width: 12px; height: 12px; background: var(--blue); flex: none; }
  .brand-name { font-weight: 400; color: var(--ink); white-space: nowrap; }
  .brand-tag { font-size: 8px; color: var(--muted); letter-spacing: .04em; margin-top: 2px; }

  .letterhead {
    position: absolute; left: 40px; top: 38px; width: 471px; height: 610px;
    background: linear-gradient(180deg, var(--white), var(--sheet));
    box-shadow: 0 2px 4px rgba(0,0,0,.25);
  }
  .letterhead .logo-block { position: absolute; right: 20px; top: 62px; }
  .letterhead .brand-name { font-size: 19px; }
  .footer-lines {
    position: absolute; font-size: 8px; line-height: 11px; color: var(--muted);
    letter-spacing: .03em;
  }
  .letterhead .footer-lines { left: 0; right: 0; bottom: 24px; text-align: center; }

  .card {
    position: absolute; top: 81px; width: 299px; height: 171px;
    background: var(--card); border-radius: 10px;
    box-shadow: 0 2px 4px rgba(0,0,0,.3);
  }
  .card-front { left: 553px; display: flex; align-items: center; justify-content: center; }
  .card-front .brand-name { font-size: 24px; }
  .card-front .brand-square { width: 18px; height: 18px; }
  .card-front .brand-tag { font-size: 10px; margin-left: 25px; }
  .card-back { left: 864px; }
  .card-back .logo-block { position: absolute; right: 16px; top: 26px; }
  .card-back .brand-name { font-size: 15px; }
  .card-back .brand-square { width: 10px; height: 10px; }
  .card-back .brand-tag { font-size: 7px; margin-left: 17px; }
  .holder { position: absolute; left: 16px; top: 38px; }
  .holder-name { font-size: 12px; font-weight: 500; color: var(--blue); }
  .holder-role { font-size: 7px; color: var(--muted); margin-top: 1px; }
  .card-back .address, .card-back .contact {
    position: absolute; font-size: 7px; line-height: 10.5px; color: var(--muted);
  }
  .card-back .address { left: 16px; top: 114px; }
  .card-back .divider {
    position: absolute; left: 147px; top: 109px; width: 3px; height: 43px;
    background: linear-gradient(var(--blue) 0 50%, var(--dark) 50% 100%);
  }
  .card-back .contact { left: 170px; top: 109px; }

  .envelope-flap { position: absolute; left: 553px; top: 295px; }
  .envelope {
    position: absolute; left: 553px; top: 371px; width: 610px; height: 277px;
    background: var(--white);
    box-shadow: 0 2px 4px rgba(0,0,0,.25);
  }
  .envelope .logo-block { position: absolute; left: 18px; top: 32px; }
  .envelope .brand-name { font-size: 17px; }
  .envelope .footer-lines { left: 18px; bottom: 18px; }
</style>
</head>
<body>

  <section class="letterhead">
    <div class="logo-block">
      <div class="brand"><span class="brand-square"></span><span class="brand-name">Harville Corp</span></div>
      <div class="brand-tag">Fencing • Security • Civil</div>
    </div>
    <div class="footer-lines">
      <p>Sydney CBD Office: 58 Harlow Street, Redfern, NSW 2016</p>
      <p>Tel.: + 02 9400 1234 | Fax: +420 311 554 207 | email@harvillecorp.com.au</p>
      <p>www.harvillecorp.com.au</p>
    </div>
    <div class="stripe"></div>
  </section>

  <section class="card card-front">
    <div class="logo-block">
      <div class="brand"><span class="brand-square"></span><span class="brand-name">Harville Corp</span></div>
      <div class="brand-tag">Fencing • Security • Civil</div>
    </div>
  </section>

  <section class="card card-back">
    <div class="holder">
      <p class="holder-name">Marek Lindqvist</p>
      <p class="holder-role">Sr. Executive</p>
    </div>
    <div class="logo-block">
      <div class="brand"><span class="brand-square"></span><span class="brand-name">Harville Corp</span></div>
      <div class="brand-tag">Fencing • Security • Civil</div>
    </div>
    <div class="address">
      <p>Sydney CBD Office:</p>
      <p>58 Harlow Street</p>
      <p>Redfern, NSW 2016</p>
    </div>
    <div class="divider"></div>
    <div class="contact">
      <p>Tel.: + 02 9400 1234</p>
      <p>Fax: +420 311 554 207</p>
      <p>email@harvillecorp.com.au</p>
      <p>www.harvillecorp.com.au</p>
    </div>
  </section>

  <svg class="envelope-flap" width="610" height="76" viewBox="0 0 610 76" aria-hidden="true">
    <path d="M0 48 C180 2 400 -14 610 48 L610 76 L0 76 Z" fill="var(--flap)"/>
  </svg>
  <section class="envelope">
    <div class="logo-block">
      <div class="brand"><span class="brand-square"></span><span class="brand-name">Harville Corp</span></div>
      <div class="brand-tag">Fencing • Security • Civil</div>
    </div>
    <div class="footer-lines">
      <p>Sydney CBD Office: 58 Harlow Street, Redfern, NSW 2016</p>
      <p>Tel.: + 02 9400 1234 | Fax: +420 311 554 207 | email@harvillecorp.com.au</p>
      <p>www.harvillecorp.com.au</p>
    </div>
    <div class="stripe"></div>
  </section>

</body>
</html>
```